Kestrel Bridge Consulting (KBC) Business Card Design

I would like to create double-sided business cards that contain:
1) Name: Derek Molvane
2) Phone Number: +1 (555) 218-4907
3) Email: Derek.Molvane@KestrelBridgeConsulting.example
4) Website: KestrelBridgeConsulting.example

I would like to include my logo and a color scheme similar to the Varnholt Grand Prix Ostera squad color scheme (black, silver, greenish-blue – but can also include regular blue)

What we do: Our company develops and delivers innovative and pragmatic information technology and cybersecurity risk and compliance solutions for organizations in the commercial market as well as the federal, and state/local sectors.

```html
<!DOCTYPE html>
<html lang="en">
<head>
<meta charset="utf-8">
<title>Kestrel Bridge Consulting — Business Card</title>
<link href="https://fonts.googleapis.com/css2?family=Montserrat:wght@400;500;700;800&display=swap" rel="stylesheet">
<style>
  :root {
    --ink: #0b0b0c;
    --paper: #f6f6f5;
    --teal: #1fa99b;
    --blue: #4b87bf;
    --navy: #1d3f78;
    --stage: #e6e6e3;
    --muted: #2a2a2e;
  }
  * { box-sizing: border-box; margin: 0; padding: 0; }
  html, body { width: 1200px; height: 900px; overflow: hidden; }
  body {
    background: var(--stage);
    font-family: "Montserrat", sans-serif;
    display: flex;
    flex-direction: column;
    align-items: center;
    justify-content: center;
    gap: 40px;
  }
  .card {
    position: relative;
    width: 700px;
    height: 400px;
    background: var(--paper);
    overflow: hidden;
    box-shadow: 0 6px 18px rgba(0,0,0,.18);
  }

  /* decorative hexagon field areas */
  .pattern-field {
    position: absolute;
    background:
      radial-gradient(circle at 40% 30%, rgba(75,135,191,.55), rgba(75,135,191,0) 60%),
      radial-gradient(circle at 60% 75%, rgba(31,169,155,.5), rgba(31,169,155,0) 60%);
  }

  /* contact side */
  .contact-side .side-shape { position: absolute; inset: 0; }
  .contact-side .brand-name {
    position: absolute;
    left: 62px;
    top: 168px;
    display: flex;
    align-items: center;
    gap: 10px;
  }
  .brand-dot {
    width: 30px; height: 30px; border-radius: 50%;
    background: var(--teal);
    flex: none;
  }
  .brand-text {
    font-weight: 700;
    color: var(--ink);
    text-transform: uppercase;
    line-height: 1.05;
    letter-spacing: .04em;
  }
  .contact-side .brand-text { font-size: 12px; }
  .person-name {
    position: absolute;
    left: 290px;
    top: 118px;
    font-size: 32px;
    color: var(--teal);
    text-transform: uppercase;
    letter-spacing: .02em;
  }
  .person-name .given { font-weight: 800; }
  .person-name .family { font-weight: 400; }
  .contact-list {
    position: absolute;
    left: 268px;
    top: 236px;
    list-style: none;
    display: flex;
    flex-direction: column;
    gap: 16px;
  }
  .contact-list li {
    display: flex;
    align-items: center;
    gap: 12px;
    font-size: 13px;
    font-weight: 500;
    color: var(--teal);
  }
  .contact-list svg { width: 16px; height: 16px; flex: none; }
  .contact-side .pattern-field { right: 0; top: 0; width: 150px; height: 260px; }

  /* brand side */
  .brand-side .pattern-left { left: 0; top: 0; width: 190px; height: 320px; }
  .brand-side .pattern-right { right: 0; top: 40px; width: 190px; height: 280px; }
  .brand-side .brand-name {
    position: absolute;
    left: 50%;
    top: 148px;
    transform: translateX(-50%);
    display: flex;
    align-items: center;
    gap: 16px;
  }
  .brand-side .brand-dot { width: 54px; height: 54px; }
  .brand-side .brand-text { font-size: 24px; }
  .web-band {
    position: absolute;
    left: 0; right: 0; bottom: 0;
    height: 80px;
    background: var(--ink);
    display: flex;
    align-items: center;
    justify-content: center;
    color: #fff;
    font-size: 17px;
    font-weight: 500;
    letter-spacing: .3em;
  }
</style>
</head>
<body>

  <section class="card contact-side">
    <svg class="side-shape" viewBox="0 0 700 400" aria-hidden="true">
      <path d="M0 0 H130 V70 A120 120 0 0 0 150 310 H180 L210 400 H0 Z" fill="var(--ink)"/>
      <path d="M128 76 A114 114 0 0 0 150 304" fill="none" stroke="var(--ink)" stroke-width="3"/>
    </svg>
    <div class="pattern-field" role="img" aria-label="Cluster of blue and teal hexagons with network lines"></div>
    <div class="brand-name">
      <span class="brand-dot"></span>
      <span class="brand-text">Kestrel Bridge<br>Consulting</span>
    </div>
    <h1 class="person-name"><span class="given">Derek</span> <span class="family">Molvane</span></h1>
    <ul class="contact-list">
      <li>
        <svg viewBox="0 0 24 24"><path fill="var(--teal)" d="M6.6 10.8a15 15 0 0 0 6.6 6.6l2.2-2.2a1 1 0 0 1 1-.25 11.4 11.4 0 0 0 3.6.6 1 1 0 0 1 1 1V20a1 1 0 0 1-1 1A17 17 0 0 1 3 4a1 1 0 0 1 1-1h3.5a1 1 0 0 1 1 1c0 1.25.2 2.45.6 3.6a1 1 0 0 1-.25 1z"/></svg>
        +1 (555) 218-4907
      </li>
      <li>
        <svg viewBox="0 0 24 24"><path fill="var(--teal)" d="M2 5h20v14H2z"/><path d="M2 5l10 8 10-8" fill="none" stroke="#fff" stroke-width="1.8"/></svg>
        Derek.Molvane@KestrelBridgeConsulting.example
      </li>
      <li>
        <svg viewBox="0 0 24 24" fill="none" stroke="var(--teal)" stroke-width="1.8"><circle cx="12" cy="12" r="9.5"/><ellipse cx="12" cy="12" rx="4" ry="9.5"/><path d="M2.5 12h19M4 7h16M4 17h16"/></svg>
        KestrelBridgeConsulting.example
      </li>
    </ul>
  </section>

  <section class="card brand-side">
    <div class="pattern-field pattern-left" role="img" aria-label="Cascade of blue and teal hexagons with network lines"></div>
    <div class="pattern-field pattern-right" role="img" aria-label="Cascade of blue and teal hexagons with network lines"></div>
    <div class="brand-name">
      <span class="brand-dot"></span>
      <span class="brand-text">Kestrel Bridge<br>Consulting</span>
    </div>
    <div class="web-band">KestrelBridgeConsulting.example</div>
  </section>

</body>
</html>
```